Finiding oppertunites in Real Estate 6.15.20

size of ad 7” x 9.6”
1-I like the ad to stand out and attract people's attention.
2-you should be able to see the text of the ad clearly .. see the attachment anything in yellow is instructions.
3-the list of topics should not be the main part of the ad
4-if you decide you want a picture or vector of a person .. (you decide)
then it should be a white male about 25-30 years old wearing a solid white or blue shirt and not long hair.
5-leave 1 inch for footer
see attachment
Good luck

Target Market(s)

potential male students 25-35 years of age

Industry/Entity Type

Education

Requirements
Must have
• will stand out and people would want to see it.
should be able to read the words of ad
Nice to have
• how to make money in real estate on one line

```html
<!DOCTYPE html>
<html lang="en">
<head>
<meta charset="utf-8">
<title>Real Estate Career Course</title>
<link rel="stylesheet" href="https://fonts.googleapis.com/css2?family=Oswald:wght@400;500;600;700&family=Montserrat:wght@400;500;600;700&display=swap">
<style>
  :root {
    --navy: #2b4a8b;
    --navy-deep: #1f3a73;
    --sky: #1ca7e1;
    --red: #e31e24;
    --grey-text: #7d7d7d;
    --grey-line: #b9b9b9;
    --grey-panel: #ececec;
    --white: #ffffff;
  }
  * { margin: 0; padding: 0; box-sizing: border-box; }
  html, body { width: 910px; height: 1200px; overflow: hidden; background: var(--white); }
  .flyer {
    position: relative; width: 910px; height: 1200px; overflow: hidden;
    background: var(--white);
    font-family: "Oswald", "Arial Narrow", sans-serif;
  }
  .flyer p, .flyer span, .flyer li, .flyer h2 { white-space: nowrap; }

  /* Header band */
  .header-band {
    position: absolute; left: 0; top: 0; width: 910px; height: 385px;
    background: linear-gradient(160deg, #34579a 0%, #2b4a8b 55%, #243f7a 100%);
  }
  .title {
    position: absolute; left: 0; width: 910px; text-align: center; display: block;
    color: var(--sky); font-weight: 700; font-size: 90px; line-height: 90px; letter-spacing: 2px;
    text-shadow: 2px 3px 4px rgba(0,0,0,.35);
  }
  .title--line1 { top: 40px; }
  .title--line2 { top: 129px; letter-spacing: 3px; }
  .tagline-rule { position: absolute; left: 130px; width: 648px; height: 2px; background: var(--white); opacity: .9; }
  .tagline-rule--top { top: 236px; }
  .tagline-rule--bottom { top: 290px; }
  .tagline {
    position: absolute; top: 241px; left: 0; width: 910px; text-align: center;
    font-size: 42px; font-weight: 600; line-height: 42px; color: var(--white);
  }
  .tagline em { font-style: normal; color: var(--sky); }

  /* Model photo */
  .model-photo {
    position: absolute; left: 490px; top: 317px; width: 368px; height: 587px;
    border-radius: 140px 140px 0 0;
    background: linear-gradient(180deg, #3a2c26 0%, #c99f86 18%, #e2c2ae 30%, #2f62b5 46%, #2a57a4 75%, #244c93 100%);
  }

  /* Remote badge */
  .remote-badge { position: absolute; left: 463px; top: 479px; width: 120px; height: 120px; }
  .remote-badge__text {
    position: absolute; left: 0; top: 37px; width: 120px; text-align: center;
    color: var(--white); font-size: 19px; font-weight: 600; line-height: 22px;
  }

  /* Intro copy */
  .audience {
    position: absolute; left: 106px; top: 431px; width: 320px; text-align: center;
    color: var(--grey-text); font-size: 20px; font-weight: 500; line-height: 25px;
  }
  .promise {
    position: absolute; left: 96px; top: 496px; width: 340px; text-align: center;
    color: var(--navy); font-size: 33px; font-weight: 700; line-height: 36px;
  }
  .sessions { position: absolute; left: 157px; top: 616px; height: 84px; width: 240px; }
  .sessions__count {
    position: absolute; left: 0; top: 0; color: var(--sky); font-size: 84px; font-weight: 700;
    line-height: 84px; text-shadow: 2px 3px 3px rgba(0,0,0,.25);
  }
  .sessions__label {
    position: absolute; left: 88px; top: 43px; height: 36px; padding: 0 8px;
    background: var(--grey-panel); color: var(--navy); font-size: 30px; font-weight: 700; line-height: 36px;
  }
  .start-date {
    position: absolute; left: 96px; top: 701px; width: 340px; text-align: center;
    color: var(--navy); font-size: 34px; font-weight: 700; line-height: 38px;
  }
  .start-date em { font-style: normal; color: var(--sky); }

  /* Partner */
  .partner { position: absolute; left: 124px; top: 790px; height: 48px; display: flex; align-items: center; gap: 12px; }
  .partner__mark { width: 40px; height: 40px; background: #2a2a2a; }
  .partner__name { color: #2a2a2a; font-size: 34px; font-weight: 500; letter-spacing: 1px; line-height: 40px; }

  /* Topics */
  .topics-heading {
    position: absolute; left: 83px; top: 886px; color: var(--sky);
    font-size: 22px; font-weight: 600; line-height: 26px;
  }
  .topics-rule { position: absolute; left: 340px; top: 906px; width: 505px; height: 1px; background: var(--grey-line); }
  .topics { position: absolute; left: 84px; top: 925px; width: 780px; height: 100px; }
  .topics__col { position: absolute; top: 0; list-style: none; }
  .topics__col:nth-child(1) { left: 0; }
  .topics__col:nth-child(2) { left: 220px; }
  .topics__col:nth-child(3) { left: 444px; }
  .topics__col:nth-child(4) { left: 611px; }
  .topics__item {
    display: flex; align-items: center; gap: 8px; height: 24.5px;
    color: #5d5d5d; font-size: 16px; font-weight: 500; line-height: 20px;
  }
  .topics__tick { width: 11px; height: 11px; flex: none; }

  /* Footer */
  .footer { position: absolute; left: 0; top: 1057px; width: 910px; height: 97px; background: #f1f1f1; }
  .footer__org {
    position: absolute; left: 0; top: 0; width: 344px; height: 97px; background: var(--navy);
    clip-path: polygon(0 0, 100% 0, 96.5% 100%, 0 100%);
  }
  .footer__brand { position: absolute; left: 34px; top: 14px; display: flex; align-items: center; gap: 10px; }
  .footer__brand-mark { width: 34px; height: 34px; background: var(--sky); }
  .footer__brand-name {
    font-family: "Montserrat", Arial, sans-serif; font-weight: 600; color: var(--white);
    font-size: 14px; line-height: 18px; letter-spacing: .3px; white-space: nowrap;
  }
  .footer__parent {
    position: absolute; left: 36px; top: 62px; width: 266px; height: 18px; background: #e9e9e9;
    color: var(--navy-deep); font-family: "Montserrat", Arial, sans-serif; font-size: 11px; font-weight: 500;
    line-height: 18px; text-align: center;
    clip-path: polygon(2% 0, 100% 0, 98% 100%, 0 100%);
  }
  .footer__contact { position: absolute; left: 350px; top: 10px; width: 380px; height: 80px; font-family: "Montserrat", Arial, sans-serif; color: var(--navy); font-size: 13.5px; font-weight: 400; }
  .contact-line { position: absolute; display: flex; align-items: center; gap: 5px; white-space: nowrap; line-height: 20px; }
  .contact-line strong { font-weight: 700; }
  .contact-icon { width: 20px; height: 20px; flex: none; }
  .footer__audience {
    position: absolute; left: 732px; top: 0; width: 178px; height: 97px; background: var(--sky);
    clip-path: polygon(8% 0, 100% 0, 100% 100%, 0 100%);
    color: var(--white); font-family: "Montserrat", Arial, sans-serif; font-weight: 600;
    font-size: 18px; line-height: 20px; text-align: center; padding: 18px 0 0 12px;
  }
  .sponsor {
    position: absolute; left: 0; top: 1168px; width: 910px; text-align: center;
    font-family: "Montserrat", Arial, sans-serif; font-size: 12px; font-weight: 500; color: #111;
  }
</style>
</head>
<body>
<main class="flyer">
  <div class="header-band" role="img" aria-label="Blue-tinted photo of architectural blueprints with a small house model, magnifier and pen"></div>

  <h1>
    <span class="title title--line1">REAL ESTATE</span>
    <span class="title title--line2">CAREER COURSE</span>
  </h1>
  <div class="tagline-rule tagline-rule--top"></div>
  <p class="tagline">HOW TO <em>MAKE MONEY</em> IN REAL ESTATE</p>
  <div class="tagline-rule tagline-rule--bottom"></div>

  <div class="model-photo" role="img" aria-label="Photo of a smiling young man with short dark hair in a blue suit, arms crossed, giving a thumbs up"></div>

  <div class="remote-badge">
    <svg width="120" height="120" viewBox="0 0 120 120" aria-hidden="true">
      <circle cx="60" cy="60" r="58" fill="#ffffff" stroke="#c9c9c9" stroke-width="3"/>
      <circle cx="60" cy="60" r="51" fill="#e31e24"/>
    </svg>
    <p class="remote-badge__text">REMOTE<br>SESSIONS</p>
  </div>

  <p class="audience">FOR THOSE WHO HAVE STARTED OR<br>WOULD LIKE TO GO INTO REAL ESTATE</p>
  <p class="promise">AN INVESTMENT IN<br>KNOWLEDGE OPENS UP<br>UNTOLD OPPORTUNITIES</p>

  <div class="sessions">
    <span class="sessions__count">12</span>
    <span class="sessions__label">SESSION</span>
  </div>
  <p class="start-date">STARTING <em>JUNE 16</em></p>

  <div class="partner">
    <span class="partner__mark"></span>
    <span class="partner__name">HARBORLINE CAPITAL</span>
  </div>

  <h2 class="topics-heading">A PARTIAL LISTING OF TOPICS</h2>
  <div class="topics-rule"></div>
  <div class="topics">
    <ul class="topics__col">
      <li class="topics__item"><svg class="topics__tick" viewBox="0 0 12 12"><circle cx="6" cy="6" r="6" fill="#1ca7e1"/><path d="M3.2 6.2l1.9 1.8 3.7-3.8" fill="none" stroke="#fff" stroke-width="1.6"/></svg>SINGLEFAMILY</li>
      <li class="topics__item"><svg class="topics__tick" viewBox="0 0 12 12"><circle cx="6" cy="6" r="6" fill="#1ca7e1"/><path d="M3.2 6.2l1.9 1.8 3.7-3.8" fill="none" stroke="#fff" stroke-width="1.6"/></svg>MULTIFAMILY</li>
      <li class="topics__item"><svg class="topics__tick" viewBox="0 0 12 12"><circle cx="6" cy="6" r="6" fill="#1ca7e1"/><path d="M3.2 6.2l1.9 1.8 3.7-3.8" fill="none" stroke="#fff" stroke-width="1.6"/></svg>MANAGEMENT</li>
      <li class="topics__item"><svg class="topics__tick" viewBox="0 0 12 12"><circle cx="6" cy="6" r="6" fill="#1ca7e1"/><path d="M3.2 6.2l1.9 1.8 3.7-3.8" fill="none" stroke="#fff" stroke-width="1.6"/></svg>REAL ESTATE CONCEPTS</li>
    </ul>
    <ul class="topics__col">
      <li class="topics__item"><svg class="topics__tick" viewBox="0 0 12 12"><circle cx="6" cy="6" r="6" fill="#1ca7e1"/><path d="M3.2 6.2l1.9 1.8 3.7-3.8" fill="none" stroke="#fff" stroke-width="1.6"/></svg>REAL ESTATE LAW</li>
      <li class="topics__item"><svg class="topics__tick" viewBox="0 0 12 12"><circle cx="6" cy="6" r="6" fill="#1ca7e1"/><path d="M3.2 6.2l1.9 1.8 3.7-3.8" fill="none" stroke="#fff" stroke-width="1.6"/></svg>INVESTMENT PROPERTIES</li>
      <li class="topics__item"><svg class="topics__tick" viewBox="0 0 12 12"><circle cx="6" cy="6" r="6" fill="#1ca7e1"/><path d="M3.2 6.2l1.9 1.8 3.7-3.8" fill="none" stroke="#fff" stroke-width="1.6"/></svg>FORECLOSURES</li>
      <li class="topics__item"><svg class="topics__tick" viewBox="0 0 12 12"><circle cx="6" cy="6" r="6" fill="#1ca7e1"/><path d="M3.2 6.2l1.9 1.8 3.7-3.8" fill="none" stroke="#fff" stroke-width="1.6"/></svg>REHAB</li>
    </ul>
    <ul class="topics__col">
      <li class="topics__item"><svg class="topics__tick" viewBox="0 0 12 12"><circle cx="6" cy="6" r="6" fill="#1ca7e1"/><path d="M3.2 6.2l1.9 1.8 3.7-3.8" fill="none" stroke="#fff" stroke-width="1.6"/></svg>FORECLOSURES</li>
      <li class="topics__item"><svg class="topics__tick" viewBox="0 0 12 12"><circle cx="6" cy="6" r="6" fill="#1ca7e1"/><path d="M3.2 6.2l1.9 1.8 3.7-3.8" fill="none" stroke="#fff" stroke-width="1.6"/></svg>SHORT SALES</li>
      <li class="topics__item"><svg class="topics__tick" viewBox="0 0 12 12"><circle cx="6" cy="6" r="6" fill="#1ca7e1"/><path d="M3.2 6.2l1.9 1.8 3.7-3.8" fill="none" stroke="#fff" stroke-width="1.6"/></svg>DEVELOPMENT</li>
      <li class="topics__item"><svg class="topics__tick" viewBox="0 0 12 12"><circle cx="6" cy="6" r="6" fill="#1ca7e1"/><path d="M3.2 6.2l1.9 1.8 3.7-3.8" fill="none" stroke="#fff" stroke-width="1.6"/></svg>FINICAL MODELING</li>
    </ul>
    <ul class="topics__col">
      <li class="topics__item"><svg class="topics__tick" viewBox="0 0 12 12"><circle cx="6" cy="6" r="6" fill="#1ca7e1"/><path d="M3.2 6.2l1.9 1.8 3.7-3.8" fill="none" stroke="#fff" stroke-width="1.6"/></svg>HUD PROPERTIES</li>
      <li class="topics__item"><svg class="topics__tick" viewBox="0 0 12 12"><circle cx="6" cy="6" r="6" fill="#1ca7e1"/><path d="M3.2 6.2l1.9 1.8 3.7-3.8" fill="none" stroke="#fff" stroke-width="1.6"/></svg>DUE DILIGENCE</li>
    </ul>
  </div>

  <footer class="footer">
    <div class="footer__org">
      <div class="footer__brand">
        <span class="footer__brand-mark"></span>
        <span class="footer__brand-name">BRIDGEWAY<br>CAREER CENTER</span>
      </div>
      <p class="footer__parent">A NON-PROFIT OF COMMUNITY UNITED</p>
    </div>

    <div class="footer__contact">
      <p class="contact-line" style="left:24px; top:0;">
        <svg class="contact-icon" viewBox="0 0 20 20"><circle cx="10" cy="10" r="9" fill="none" stroke="#1ca7e1" stroke-width="1.3"/><path d="M10 15.5s-4-4.3-4-7a4 4 0 0 1 8 0c0 2.7-4 7-4 7z" fill="none" stroke="#2b4a8b" stroke-width="1.3"/><circle cx="10" cy="8.4" r="1.4" fill="#2b4a8b"/></svg>
        Eastport - Riverton - Millbrook, <strong>Main Branch</strong>
      </p>
      <p class="contact-line" style="left:20px; top:25px;">
        <svg class="contact-icon" viewBox="0 0 20 20"><circle cx="10" cy="10" r="9" fill="none" stroke="#1ca7e1" stroke-width="1.3"/><circle cx="10" cy="10" r="5.5" fill="none" stroke="#2b4a8b" stroke-width="1.1"/><ellipse cx="10" cy="10" rx="2.4" ry="5.5" fill="none" stroke="#2b4a8b" stroke-width="1"/><path d="M4.5 10h11M5.3 7.3h9.4M5.3 12.7h9.4" stroke="#2b4a8b" stroke-width="1"/></svg>
        www.bwcc.org
        <svg class="contact-icon" viewBox="0 0 20 20" style="margin-left:10px"><circle cx="10" cy="10" r="9" fill="none" stroke="#1ca7e1" stroke-width="1.3"/><path d="M6.5 5.5l2 -.3 1.2 2.8-1.3 1c.6 1.3 1.5 2.2 2.6 2.7l1-1.3 2.8 1.2-.3 2c-4.5.3-8.3-3.6-8-8.1z" fill="none" stroke="#2b4a8b" stroke-width="1.1" stroke-linejoin="round"/></svg>
        555 010 2400 x 610
      </p>
      <p class="contact-line" style="left:16px; top:50px;">
        <svg class="contact-icon" viewBox="0 0 20 20"><circle cx="10" cy="10" r="9" fill="none" stroke="#1ca7e1" stroke-width="1.3"/><rect x="5" y="6.5" width="10" height="7" rx="1" fill="#1ca7e1"/><path d="M5.3 7l4.7 3.6L14.7 7" fill="none" stroke="#fff" stroke-width="1"/></svg>
        info@bwcc.org
      </p>
    </div>

    <p class="footer__audience">MEN &amp;<br>WOMEN<br>CLASSES</p>
  </footer>

  <p class="sponsor">Bridgeway Career Center is sponsored in part by the Harlan Whitfield family foundation.</p>
</main>
</body>
</html>
```